RVM Photography Business Card Design

I would like a business card designed in the shape of a camera.
Would like to see various camera designs. Would like to see what the card looks like in different colors. Would like to see which logo looks better on the various camera designs so please show me some with the white logo and some with the black logo. If you need a different file formats please let me know.
Project Deadline Extended Reason: My grandfather passed away and dealing with funeral plans so need to extend deadline. Added Tuesday, March 1, 2016
Project Deadline Extended
Reason: I just got back from out of town. My grandfather's passing was the primary focus for me these past few weeks and the funeral is over so now I will concentrate on picking my business card design. I really appreciate each designer who has taken the time to submit a design. Your effort has not gone unnoticed. I look forward to seeing more amazing designs.
Industry/Entity Type
Business
Contact Information for Business Card
Corinne
757-418-2296
https://www.facebook.com/rvmphotographyfreelance/
NoraCorinne@rvm-studiowork.example

```html
<!DOCTYPE html>
<html lang="en">
<head>
<meta charset="utf-8">
<title>RVM Photography Business Card</title>
<link rel="stylesheet" href="https://fonts.googleapis.com/css2?family=Cinzel:wght@400&family=Open+Sans:wght@400;700&display=swap">
<style>
  :root {
    --backdrop: #bbbcbe;
    --card-black: #020202;
    --accent-amber: #c17f31;
    --logo-gold: #d6a33a;
    --paper-white: #ffffff;
  }
  html, body {
    margin: 0;
    padding: 0;
    overflow: hidden;
  }
  body {
    width: 1200px;
    height: 927px;
    background: var(--backdrop);
    position: relative;
  }
  .camera-card {
    position: absolute;
    top: 290px;
    width: 543px;
    height: 347px;
  }
  .camera-card--amber { left: 42px; }
  .camera-card--white { left: 615px; }
  .camera-shape {
    position: absolute;
    inset: 0;
    filter: drop-shadow(6px 8px 6px rgba(0,0,0,0.35));
  }
  .brand-mark {
    position: absolute;
    left: 412px;
    top: 44px;
    width: 74px;
    height: 74px;
    border-radius: 50%;
    background: var(--logo-gold);
  }
  .brand-name {
    position: absolute;
    left: 292px;
    top: 121px;
    width: 240px;
    text-align: center;
    font-family: "Cinzel", serif;
    font-weight: 400;
    font-size: 21px;
    color: var(--logo-gold);
    white-space: nowrap;
  }
  .holder {
    position: absolute;
    left: 81px;
    top: 262px;
    font-family: "Open Sans", sans-serif;
  }
  .holder-name {
    margin: 0 0 6px;
    font-size: 21px;
    font-weight: 700;
    letter-spacing: 1.6px;
    line-height: 26px;
  }
  .contact-line {
    display: flex;
    align-items: center;
    gap: 10px;
    font-size: 13.5px;
    letter-spacing: 0.6px;
    line-height: 17px;
  }
  .contact-line svg { width: 12px; height: 12px; }
  .camera-card--amber .holder { color: var(--accent-amber); }
  .camera-card--white .holder { color: var(--paper-white); }
</style>
</head>
<body>

<div class="camera-card camera-card--amber">
  <svg class="camera-shape" viewBox="0 0 543 347" width="543" height="347">
    <rect x="70" y="15" width="65" height="24" rx="6" fill="var(--card-black)"/>
    <rect x="383" y="0" width="104" height="34" rx="10" fill="var(--card-black)"/>
    <rect x="0" y="21" width="543" height="326" rx="22" fill="var(--card-black)"/>
    <rect x="29" y="21" width="35" height="326" fill="var(--accent-amber)"/>
  </svg>
  <div class="brand-mark"></div>
  <div class="brand-name">RVM PHOTOGRAPHY</div>
  <div class="holder">
    <p class="holder-name">DALE FENWICK</p>
    <div class="contact-line">
      <svg viewBox="0 0 12 12" aria-hidden="true"><path d="M2.5 1 L4.5 1 L5 3.5 L3.8 4.4 Q5 7 7.6 8.2 L8.5 7 L11 7.5 L11 9.5 Q10.5 11 9 11 Q2 10 1 3 Q1 1.5 2.5 1 Z" fill="currentColor"/></svg>
      <span>+330 2815-4392</span>
    </div>
    <div class="contact-line">
      <svg viewBox="0 0 12 12" aria-hidden="true"><rect x="1" y="2.5" width="10" height="7" fill="none" stroke="currentColor" stroke-width="1.1"/><path d="M1 2.5 L6 6.5 L11 2.5" fill="none" stroke="currentColor" stroke-width="1.1"/></svg>
      <span>dale@fenwickmail.example</span>
    </div>
  </div>
</div>

<div class="camera-card camera-card--white">
  <svg class="camera-shape" viewBox="0 0 543 347" width="543" height="347">
    <rect x="70" y="15" width="65" height="24" rx="6" fill="var(--card-black)"/>
    <rect x="383" y="0" width="104" height="34" rx="10" fill="var(--card-black)"/>
    <rect x="0" y="21" width="543" height="326" rx="22" fill="var(--card-black)"/>
    <rect x="29" y="21" width="35" height="326" fill="var(--paper-white)"/>
  </svg>
  <div class="brand-mark"></div>
  <div class="brand-name">RVM PHOTOGRAPHY</div>
  <div class="holder">
    <p class="holder-name">DALE FENWICK</p>
    <div class="contact-line">
      <svg viewBox="0 0 12 12" aria-hidden="true"><path d="M2.5 1 L4.5 1 L5 3.5 L3.8 4.4 Q5 7 7.6 8.2 L8.5 7 L11 7.5 L11 9.5 Q10.5 11 9 11 Q2 10 1 3 Q1 1.5 2.5 1 Z" fill="currentColor"/></svg>
      <span>+330 2815-4392</span>
    </div>
    <div class="contact-line">
      <svg viewBox="0 0 12 12" aria-hidden="true"><rect x="1" y="2.5" width="10" height="7" fill="none" stroke="currentColor" stroke-width="1.1"/><path d="M1 2.5 L6 6.5 L11 2.5" fill="none" stroke="currentColor" stroke-width="1.1"/></svg>
      <span>dale@fenwickmail.example</span>
    </div>
  </div>
</div>

</body>
</html>
```